Fold & Puff Disposable Marijuana Pipe

The product is a reusable / Disposable Marijuana pipe design for retail sales where Marijuana is legalized. The product come 3-pipes on a sheet and are separated on the perforations. The product is called "Fold & Puff" but I'm open to other ideas. Each card can be the same design or they can be different, the goal is to project a cool factor as well as convenience - Each pipe is exactly the size of a business card so they can be easily put in a wallet.

Target Market(s)

Medical and Recreational Marijuana smokers

```html
<!DOCTYPE html>
<html lang="en">
<head>
<meta charset="utf-8">
<title>Fold &amp; Puff – Pipe Sheets</title>
<link href="https://fonts.googleapis.com/css2?family=Anton&family=Montserrat:wght@500;700&display=swap" rel="stylesheet">
<style>
  :root {
    --canvas: #ebebeb;
    --paper: #f5f5f5;
    --mint: #46d494;
    --mint-deep: #35a06f;
    --slate: #5a7a6a;
    --amber: #f7b862;
    --amber-deep: #e0a34f;
    --amber-soft: #fbe3bd;
    --dot: #c8842a;
    --rule-dark: #6e4a22;
    --guide: #f0b04a;
    --ribbon: #d8262c;
    --price: #f5a623;
    --ink: #1f3a2c;
    --white: #ffffff;
  }
  * { margin: 0; padding: 0; box-sizing: border-box; }
  html, body { width: 1163px; height: 1200px; overflow: hidden; background: var(--canvas); }
  .stage {
    position: relative; width: 1454px; height: 1500px;
    transform: scale(0.8); transform-origin: 0 0;
  }
  .sheet {
    position: absolute; top: 78px; width: 610px; height: 1342px;
    background: var(--paper); overflow: hidden;
    font-family: "Montserrat", sans-serif;
  }
  .sheet--left { left: 82px; }
  .sheet--right { left: 760px; }

  .header { position: absolute; left: 0; top: 0; width: 610px; height: 233px; background: var(--mint); }
  .header__art { position: absolute; left: 0; top: 0; }
  .count-badge {
    position: absolute; left: 16px; top: 16px; width: 84px; height: 84px; border-radius: 50%;
    background: var(--ribbon); border: 4px solid #2a2a2a; box-shadow: 0 0 0 3px var(--white) inset;
    color: var(--white); text-align: center;
  }
  .count-badge__num { display: block; font-family: "Anton", sans-serif; font-size: 38px; line-height: 1; margin-top: 10px; }
  .count-badge__label { display: block; font-size: 10px; font-weight: 700; letter-spacing: 0.5px; }
  .price {
    position: absolute; left: 495px; top: 45px; width: 110px; text-align: center;
    font-family: "Anton", sans-serif; font-size: 40px; color: var(--price);
    transform: rotate(45deg);
  }
  .brand {
    position: absolute; left: 0; top: 100px; width: 610px; text-align: center;
    font-family: "Anton", sans-serif; font-size: 86px; line-height: 1; color: var(--white);
    text-transform: uppercase; letter-spacing: 2px;
  }
  .tagline {
    position: absolute; left: 0; top: 197px; width: 610px; text-align: center;
    font-size: 20px; font-weight: 500; letter-spacing: 5px; color: var(--ink);
  }

  .pipe { position: absolute; left: 0; width: 610px; height: 369px; }
  .pipe--1 { top: 233px; }
  .pipe--2 { top: 602px; }
  .pipe--3 { top: 971px; }
  .pipe__art { position: absolute; left: 0; top: 0; }
  .pipe__icon { position: absolute; left: 19px; top: 8px; width: 40px; height: 31px; background: var(--amber); border-radius: 4px; }
  .pipe__label {
    position: absolute; left: 112px; top: 0; height: 47px; line-height: 47px;
    font-size: 18px; font-weight: 500; letter-spacing: 3px; color: var(--white);
  }
  .pipe__brand {
    position: absolute; left: 150px; top: 144px; width: 226px; text-align: center;
    font-family: "Anton", sans-serif; font-size: 38px; line-height: 1; color: var(--guide);
    text-transform: uppercase;
  }
  .pipe__fold-guide {
    position: absolute; left: 446px; top: 126px; width: 128px; height: 82px;
    background: var(--amber-soft);
  }
</style>
</head>
<body>
<div class="stage">

  <div class="sheet sheet--left">
    <header class="header">
      <svg class="header__art" width="610" height="233" viewBox="0 0 610 233">
        <path d="M205 90 Q205 81 215 78 L307 52 L399 78 Q409 81 409 90 L409 97 Q409 105 400 105 L214 105 Q205 105 205 97 Z" fill="var(--mint-deep)"/>
        <polygon points="430,0 510,0 610,100 610,180" fill="var(--ribbon)"/>
        <line x1="440" y1="4" x2="606" y2="170" stroke="#fff" stroke-width="1.5" stroke-dasharray="5 4" opacity="0.8"/>
        <line x1="500" y1="4" x2="606" y2="110" stroke="#fff" stroke-width="1.5" stroke-dasharray="5 4" opacity="0.8"/>
      </svg>
      <div class="count-badge"><span class="count-badge__num">#3</span><span class="count-badge__label">PIPES</span></div>
      <div class="price">$2.99</div>
      <h1 class="brand">Fold &amp; Puff</h1>
      <p class="tagline">Reusable / Disposable Pipes</p>
    </header>

    <section class="pipe pipe--1">
      <svg class="pipe__art" width="610" height="369" viewBox="0 0 610 369">
        <rect x="0" y="0" width="78" height="369" fill="var(--amber)"/>
        <rect x="0" y="0" width="78" height="47" fill="var(--amber-deep)"/>
        <rect x="78" y="0" width="532" height="47" fill="var(--slate)"/>
        <g fill="var(--dot)"><circle cx="16" cy="66" r="8.5"/><circle cx="62" cy="66" r="8.5"/><circle cx="38" cy="87" r="8.5"/><circle cx="16" cy="108" r="8.5"/><circle cx="62" cy="108" r="8.5"/><circle cx="38" cy="249" r="8.5"/></g>
        <g stroke="var(--mint)" stroke-width="1.5" stroke-dasharray="6 4"><line x1="78" y1="126" x2="610" y2="126"/><line x1="78" y1="208" x2="610" y2="208"/><line x1="78" y1="288" x2="610" y2="288"/></g>
        <g stroke="var(--rule-dark)" stroke-width="1.5" stroke-dasharray="6 3"><line x1="0" y1="126" x2="78" y2="126"/><line x1="0" y1="208" x2="78" y2="208"/><line x1="0" y1="288" x2="78" y2="288"/></g>
        <g stroke="var(--slate)" stroke-width="2" fill="none"><line x1="71" y1="318" x2="82" y2="345"/><line x1="85" y1="318" x2="74" y2="345"/><circle cx="72" cy="350" r="4.5"/><circle cx="84" cy="350" r="4.5"/></g>
      </svg>
      <div class="pipe__icon" role="img" aria-label="Leaf icon"></div>
      <h2 class="pipe__label">Double Sided Adhesive Tape w/ Backer</h2>
      <p class="pipe__brand">Fold &amp; Puff</p>
      <div class="pipe__fold-guide" role="img" aria-label="Fold guide diagram showing where to crease the pipe"></div>
    </section>

    <section class="pipe pipe--2">
      <svg class="pipe__art" width="610" height="369" viewBox="0 0 610 369">
        <rect x="0" y="0" width="78" height="369" fill="var(--amber)"/>
        <rect x="0" y="0" width="78" height="47" fill="var(--amber-deep)"/>
        <rect x="78" y="0" width="532" height="47" fill="var(--slate)"/>
        <g fill="var(--dot)"><circle cx="16" cy="66" r="8.5"/><circle cx="62" cy="66" r="8.5"/><circle cx="38" cy="87" r="8.5"/><circle cx="16" cy="108" r="8.5"/><circle cx="62" cy="108" r="8.5"/><circle cx="38" cy="249" r="8.5"/></g>
        <g stroke="var(--mint)" stroke-width="1.5" stroke-dasharray="6 4"><line x1="78" y1="126" x2="610" y2="126"/><line x1="78" y1="208" x2="610" y2="208"/><line x1="78" y1="288" x2="610" y2="288"/></g>
        <g stroke="var(--rule-dark)" stroke-width="1.5" stroke-dasharray="6 3"><line x1="0" y1="126" x2="78" y2="126"/><line x1="0" y1="208" x2="78" y2="208"/><line x1="0" y1="288" x2="78" y2="288"/></g>
        <g stroke="var(--slate)" stroke-width="2" fill="none"><line x1="71" y1="318" x2="82" y2="345"/><line x1="85" y1="318" x2="74" y2="345"/><circle cx="72" cy="350" r="4.5"/><circle cx="84" cy="350" r="4.5"/></g>
      </svg>
      <div class="pipe__icon" role="img" aria-label="Leaf icon"></div>
      <h2 class="pipe__label">Double Sided Adhesive Tape w/ Backer</h2>
      <p class="pipe__brand">Fold &amp; Puff</p>
      <div class="pipe__fold-guide" role="img" aria-label="Fold guide diagram showing where to crease the pipe"></div>
    </section>

    <section class="pipe pipe--3">
      <svg class="pipe__art" width="610" height="369" viewBox="0 0 610 369">
        <rect x="0" y="0" width="78" height="369" fill="var(--amber)"/>
        <rect x="0" y="0" width="78" height="47" fill="var(--amber-deep)"/>
        <rect x="78" y="0" width="532" height="47" fill="var(--slate)"/>
        <g fill="var(--dot)"><circle cx="16" cy="66" r="8.5"/><circle cx="62" cy="66" r="8.5"/><circle cx="38" cy="87" r="8.5"/><circle cx="16" cy="108" r="8.5"/><circle cx="62" cy="108" r="8.5"/><circle cx="38" cy="249" r="8.5"/></g>
        <g stroke="var(--mint)" stroke-width="1.5" stroke-dasharray="6 4"><line x1="78" y1="126" x2="610" y2="126"/><line x1="78" y1="208" x2="610" y2="208"/><line x1="78" y1="288" x2="610" y2="288"/></g>
        <g stroke="var(--rule-dark)" stroke-width="1.5" stroke-dasharray="6 3"><line x1="0" y1="126" x2="78" y2="126"/><line x1="0" y1="208" x2="78" y2="208"/><line x1="0" y1="288" x2="78" y2="288"/></g>
        <g stroke="var(--slate)" stroke-width="2" fill="none"><line x1="71" y1="318" x2="82" y2="345"/><line x1="85" y1="318" x2="74" y2="345"/><circle cx="72" cy="350" r="4.5"/><circle cx="84" cy="350" r="4.5"/></g>
      </svg>
      <div class="pipe__icon" role="img" aria-label="Leaf icon"></div>
      <h2 class="pipe__label">Double Sided Adhesive Tape w/ Backer</h2>
      <p class="pipe__brand">Fold &amp; Puff</p>
      <div class="pipe__fold-guide" role="img" aria-label="Fold guide diagram showing where to crease the pipe"></div>
    </section>
  </div>

  <div class="sheet sheet--right">
    <header class="header">
      <svg class="header__art" width="610" height="233" viewBox="0 0 610 233">
        <path d="M205 90 Q205 81 215 78 L307 52 L399 78 Q409 81 409 90 L409 97 Q409 105 400 105 L214 105 Q205 105 205 97 Z" fill="var(--mint-deep)"/>
        <polygon points="430,0 510,0 610,100 610,180" fill="var(--ribbon)"/>
        <line x1="440" y1="4" x2="606" y2="170" stroke="#fff" stroke-width="1.5" stroke-dasharray="5 4" opacity="0.8"/>
        <line x1="500" y1="4" x2="606" y2="110" stroke="#fff" stroke-width="1.5" stroke-dasharray="5 4" opacity="0.8"/>
      </svg>
      <div class="count-badge"><span class="count-badge__num">#3</span><span class="count-badge__label">PIPES</span></div>
      <div class="price">$2.99</div>
      <h1 class="brand">Fold &amp; Puff</h1>
      <p class="tagline">Reusable / Disposable Pipes</p>
    </header>

    <section class="pipe pipe--1">
      <svg class="pipe__art" width="610" height="369" viewBox="0 0 610 369">
        <rect x="0" y="0" width="78" height="369" fill="var(--amber)"/>
        <rect x="0" y="0" width="78" height="47" fill="var(--amber-deep)"/>
        <rect x="78" y="0" width="532" height="47" fill="var(--slate)"/>
        <g fill="var(--dot)"><circle cx="16" cy="66" r="8.5"/><circle cx="62" cy="66" r="8.5"/><circle cx="38" cy="87" r="8.5"/><circle cx="16" cy="108" r="8.5"/><circle cx="62" cy="108" r="8.5"/><circle cx="38" cy="249" r="8.5"/></g>
        <g stroke="var(--mint)" stroke-width="1.5" stroke-dasharray="6 4"><line x1="78" y1="126" x2="610" y2="126"/><line x1="78" y1="208" x2="610" y2="208"/><line x1="78" y1="288" x2="610" y2="288"/></g>
        <g stroke="var(--rule-dark)" stroke-width="1.5" stroke-dasharray="6 3"><line x1="0" y1="126" x2="78" y2="126"/><line x1="0" y1="208" x2="78" y2="208"/><line x1="0" y1="288" x2="78" y2="288"/></g>
        <g stroke="var(--slate)" stroke-width="2" fill="none"><line x1="71" y1="318" x2="82" y2="345"/><line x1="85" y1="318" x2="74" y2="345"/><circle cx="72" cy="350" r="4.5"/><circle cx="84" cy="350" r="4.5"/></g>
      </svg>
      <div class="pipe__icon" role="img" aria-label="Leaf icon"></div>
      <h2 class="pipe__label">Double Sided Adhesive Tape w/ Backer</h2>
      <p class="pipe__brand">Fold &amp; Puff</p>
      <div class="pipe__fold-guide" role="img" aria-label="Fold guide diagram showing where to crease the pipe"></div>
    </section>

    <section class="pipe pipe--2">
      <svg class="pipe__art" width="610" height="369" viewBox="0 0 610 369">
        <rect x="0" y="0" width="78" height="369" fill="var(--amber)"/>
        <rect x="0" y="0" width="78" height="47" fill="var(--amber-deep)"/>
        <rect x="78" y="0" width="532" height="47" fill="var(--slate)"/>
        <g fill="var(--dot)"><circle cx="16" cy="66" r="8.5"/><circle cx="62" cy="66" r="8.5"/><circle cx="38" cy="87" r="8.5"/><circle cx="16" cy="108" r="8.5"/><circle cx="62" cy="108" r="8.5"/><circle cx="38" cy="249" r="8.5"/></g>
        <g stroke="var(--mint)" stroke-width="1.5" stroke-dasharray="6 4"><line x1="78" y1="126" x2="610" y2="126"/><line x1="78" y1="208" x2="610" y2="208"/><line x1="78" y1="288" x2="610" y2="288"/></g>
        <g stroke="var(--rule-dark)" stroke-width="1.5" stroke-dasharray="6 3"><line x1="0" y1="126" x2="78" y2="126"/><line x1="0" y1="208" x2="78" y2="208"/><line x1="0" y1="288" x2="78" y2="288"/></g>
        <g stroke="var(--slate)" stroke-width="2" fill="none"><line x1="71" y1="318" x2="82" y2="345"/><line x1="85" y1="318" x2="74" y2="345"/><circle cx="72" cy="350" r="4.5"/><circle cx="84" cy="350" r="4.5"/></g>
      </svg>
      <div class="pipe__icon" role="img" aria-label="Leaf icon"></div>
      <h2 class="pipe__label">Double Sided Adhesive Tape w/ Backer</h2>
      <p class="pipe__brand">Fold &amp; Puff</p>
      <div class="pipe__fold-guide" role="img" aria-label="Fold guide diagram showing where to crease the pipe"></div>
    </section>

    <section class="pipe pipe--3">
      <svg class="pipe__art" width="610" height="369" viewBox="0 0 610 369">
        <rect x="0" y="0" width="78" height="369" fill="var(--amber)"/>
        <rect x="0" y="0" width="78" height="47" fill="var(--amber-deep)"/>
        <rect x="78" y="0" width="532" height="47" fill="var(--slate)"/>
        <g fill="var(--dot)"><circle cx="16" cy="66" r="8.5"/><circle cx="62" cy="66" r="8.5"/><circle cx="38" cy="87" r="8.5"/><circle cx="16" cy="108" r="8.5"/><circle cx="62" cy="108" r="8.5"/><circle cx="38" cy="249" r="8.5"/></g>
        <g stroke="var(--mint)" stroke-width="1.5" stroke-dasharray="6 4"><line x1="78" y1="126" x2="610" y2="126"/><line x1="78" y1="208" x2="610" y2="208"/><line x1="78" y1="288" x2="610" y2="288"/></g>
        <g stroke="var(--rule-dark)" stroke-width="1.5" stroke-dasharray="6 3"><line x1="0" y1="126" x2="78" y2="126"/><line x1="0" y1="208" x2="78" y2="208"/><line x1="0" y1="288" x2="78" y2="288"/></g>
        <g stroke="var(--slate)" stroke-width="2" fill="none"><line x1="71" y1="318" x2="82" y2="345"/><line x1="85" y1="318" x2="74" y2="345"/><circle cx="72" cy="350" r="4.5"/><circle cx="84" cy="350" r="4.5"/></g>
      </svg>
      <div class="pipe__icon" role="img" aria-label="Leaf icon"></div>
      <h2 class="pipe__label">Double Sided Adhesive Tape w/ Backer</h2>
      <p class="pipe__brand">Fold &amp; Puff</p>
      <div class="pipe__fold-guide" role="img" aria-label="Fold guide diagram showing where to crease the pipe"></div>
    </section>
  </div>

</div>
</body>
</html>
```